Business card for new business - financial management

I need a business card designed for my new business. I'm the owner / sole trader of QVB Consulting, which provides financial management services for Government. I'd like the design to incorporate the attached business name and colours. The design should include colour and not be too way out - it needs to look at home in a government environment.
Details to be included on the card are:
QVB Consulting
Miriam Haskett
0400 386 924
miriamrhaskett@fernmail.example
47 Pallister Crescent, Wattlegrove ACT 2611
Single or double sided designs would be good.
Employees at Australian Federal Government agencies
Government

```html
<!DOCTYPE html>
<html lang="en">
<head>
<meta charset="utf-8">
<title>QVB Consulting — Business Card</title>
<link rel="stylesheet" href="https://fonts.googleapis.com/css2?family=Open+Sans:wght@400;700&display=swap">
<style>
  :root {
    --page-bg: #ecebe8;
    --card-bg: #ffffff;
    --ink: #111111;
    --teal-dark: #1f5f6e;
    --teal: #2e8a9c;
    --sky: #90cbd8;
    --blue: #3a6795;
    --body-font: "Open Sans", Verdana, sans-serif;
  }
  * { box-sizing: border-box; margin: 0; padding: 0; }
  html, body {
    width: 1200px;
    height: 1000px;
    overflow: hidden;
    background: var(--page-bg);
  }
  .business-card {
    position: absolute;
    left: 100px;
    top: 197px;
    width: 1000px;
    height: 606px;
    background: var(--card-bg);
    box-shadow: 0 6px 24px rgba(0,0,0,0.12);
    font-family: var(--body-font);
    color: var(--ink);
    overflow: hidden;
  }
  .brand {
    position: absolute;
    left: 90px;
    top: 92px;
    display: flex;
    align-items: center;
    gap: 22px;
  }
  .brand-mark {
    width: 50px;
    height: 50px;
    background: var(--sky);
  }
  .brand-name {
    font-size: 60px;
    font-weight: 400;
    color: var(--blue);
    line-height: 1;
    letter-spacing: 0.5px;
    white-space: nowrap;
  }
  .contact {
    position: absolute;
    left: 90px;
    top: 265px;
  }
  .contact-name {
    font-size: 40px;
    font-weight: 700;
    line-height: 1.2;
    white-space: nowrap;
  }
  .contact-line {
    margin-left: 40px;
    font-size: 36px;
    line-height: 1.35;
    white-space: nowrap;
  }
  .contact-label {
    color: var(--teal-dark);
    font-weight: 700;
    margin-right: 8px;
  }
  .address {
    position: absolute;
    right: 50px;
    bottom: 78px;
    font-size: 22px;
    letter-spacing: 1px;
    white-space: nowrap;
  }
  .colour-bands {
    position: absolute;
    left: 0;
    bottom: 0;
    width: 100%;
    height: 55px;
    display: flex;
  }
  .band { flex: 1; }
  .band--teal-dark { background: var(--teal-dark); }
  .band--teal { background: var(--teal); }
  .band--sky { background: var(--sky); }
  .band--blue { background: var(--blue); }
</style>
</head>
<body>
  <article class="business-card">
    <header class="brand">
      <span class="brand-mark" aria-hidden="true"></span>
      <span class="brand-name">QVB Consulting</span>
    </header>

    <section class="contact">
      <p class="contact-name">Miriam Haskett</p>
      <p class="contact-line"><span class="contact-label">T:</span>0400 386 924</p>
      <p class="contact-line"><span class="contact-label">E:</span>miriamrhaskett@fernmail.example</p>
    </section>

    <p class="address">47 Pallister Crescent, Wattlegrove ACT 2611</p>

    <footer class="colour-bands" aria-hidden="true">
      <span class="band band--teal-dark"></span>
      <span class="band band--teal"></span>
      <span class="band band--sky"></span>
      <span class="band band--blue"></span>
    </footer>
  </article>
</body>
</html>
```